Stationary Design needed for luxorious bespoke tailor

We need a design for our stationary items like businescards, letters, envelope and letter head / Signature for email. Our company "LE CORVAN" sells exclusively and luxourious bespoke garments and accessories for men. The desgins of letterhead, envelope and business card shoulderstand communicate luxury, high quality and good taste. We would like our logo to be used on the designs.

Target Market(s)

Gentleman with a high aproach and exclusive and luxourious suits and shirts, grooms, businesman,

Industry/Entity Type

It Company

Font styles to use
Sans Serif

Colors
ec1f27
ffffff

Requirements
Must have
• Logo, Companies name and adress, contactName internet & email, phone number line / mobile, VAT Nr. On Business Card frontpage only logo and name, adress companies on backpage. No VAT and Companies ID there. Company data; LE CORVAN AG Wiesenrain 42 4057 Basel Switzerland VAT: CHE 472 916 304 Tax Tel 41 61 594 17 36 Mobile 41 79 842 06 91 www.korvanmode.ch info@korvanmode.com.
Nice to have
• -Name And phone numbers need to be able to change (for different coworkers ...)
Should not have
• no VAT in Business Card

```html
<!DOCTYPE html>
<html lang="de">
<head>
<meta charset="utf-8">
<title>LE CORVAN AG – Visitenkarte</title>
<link rel="stylesheet" href="https://fonts.googleapis.com/css2?family=Montserrat:wght@400;500;700&display=swap">
<style>
  :root {
    --backdrop: #2b2b2b;
    --card: #050505;
    --red: #ec1f27;
    --white: #ffffff;
    --soft-white: #e8e8e8;
  }
  * { margin: 0; padding: 0; box-sizing: border-box; }
  html, body {
    width: 1200px;
    height: 900px;
    overflow: hidden;
    background: var(--backdrop);
    font-family: "Montserrat", Arial, sans-serif;
  }
  .stage {
    position: relative;
    width: 1200px;
    height: 900px;
  }
  .card {
    position: absolute;
    width: 620px;
    height: 380px;
    background: var(--card);
    border-radius: 28px;
    box-shadow: 0 18px 40px rgba(0,0,0,0.55);
    color: var(--white);
  }
  .card--front { left: 290px; top: 50px; }
  .card--back  { left: 290px; top: 470px; }

  .wordmark {
    position: absolute;
    font-weight: 700;
    font-size: 44px;
    letter-spacing: 2px;
    color: var(--white);
    white-space: nowrap;
  }
  .card--front .wordmark { left: 0; right: 0; top: 140px; text-align: center; }
  .card--back .wordmark { left: 44px; top: 100px; font-size: 32px; }

  .front-web {
    position: absolute;
    right: 150px;
    top: 300px;
    font-size: 17px;
    color: var(--white);
  }
  .front-web .accent { color: var(--red); }

  .contact {
    position: absolute;
    left: 380px;
    top: 96px;
    font-size: 14px;
    line-height: 1.5;
    color: var(--soft-white);
  }
  .contact__company {
    color: var(--red);
    font-weight: 700;
    font-size: 21px;
    margin-bottom: 6px;
  }
  .contact__vat .accent { color: var(--red); }
  .contact__row {
    display: flex;
    align-items: center;
    gap: 9px;
  }
  .contact__row svg {
    width: 12px;
    height: 12px;
    flex: none;
    fill: none;
    stroke: var(--red);
    stroke-width: 2;
  }
</style>
</head>
<body>
<main class="stage">

  <section class="card card--front" aria-label="Vorderseite">
    <div class="wordmark">KORVAN MODE</div>
    <p class="front-web">www.<span class="accent">korvanmode</span>.ch</p>
  </section>

  <section class="card card--back" aria-label="Rückseite">
    <div class="wordmark">KORVAN MODE</div>
    <div class="contact">
      <p class="contact__company">LE CORVAN AG</p>
      <p>Wiesenrain 42 4057</p>
      <p>Basel Switzerland</p>
      <p class="contact__vat"><span class="accent">VAT: CHE</span> 472 916 304 TAX</p>
      <p class="contact__row">
        <svg viewBox="0 0 24 24"><path d="M5 3h4l2 5-3 2a12 12 0 0 0 6 6l2-3 5 2v4a2 2 0 0 1-2 2A18 18 0 0 1 3 5a2 2 0 0 1 2-2z"/></svg>
        41 61 594 17 36
      </p>
      <p class="contact__row">
        <svg viewBox="0 0 24 24"><rect x="6" y="2" width="12" height="20" rx="2"/><line x1="11" y1="18" x2="13" y2="18"/></svg>
        41 79 842 06 91
      </p>
      <p class="contact__row">
        <svg viewBox="0 0 24 24"><rect x="2" y="5" width="20" height="14" rx="1"/><path d="M2 6l10 7 10-7"/></svg>
        info@korvanmode.com
      </p>
      <p class="contact__row">
        <svg viewBox="0 0 24 24"><circle cx="12" cy="12" r="10"/><path d="M2 12h20M12 2a15 15 0 0 1 0 20M12 2a15 15 0 0 0 0 20"/></svg>
        www.korvanmode.ch
      </p>
    </div>
  </section>

</main>
</body>
</html>
```